Design a calming beauty medical salon & spa website based in Hong Kong

We need help building an informational website for a beauty salon in Hong Kong. The local salon provides facials, massages, body and other slimming treatments in a relaxing environment. We offer some non-invasive medical treatments, such as botox. Having built the business on word of mouth, it is now time for us to launch a website to help market the business better. Website requirements:

-Must be responsive
-Use vibrant but clean colours. not too many, 1-2 colours
-Must be bilingual (switch between Chinese traditional and English)
-Our current website is host on a server, not using any particular platforms like wordpress

Pages:
1/ Homepage
2/ About us (incorporate gallery of salon photos and history of company)
3/ Promotions and latest deals (and leads them to sign up for more info, maybe pop-up small window when you click on a promotion)
4/ Treatment menus
4.1/Body treatments
4.2/ Face treatments
4.3/ Slimming treatments
5/ Showcasing products sold (no e-commerce functionality, just showing off products)
6/ Contact us (tel, address, map, opening hrs)

Footer - must haves include contact us info, privacy policy, terms & conditions, copyright blurb, join our company/employment page (with a form)

For information (comparable websites we like):
http://vostaria.com/
http://quimbel.com.hk/tc/aboutquimbel/background.php#centerenvi
Attaching a very first draft concept for this website
Attaching pictures of the beauty salon
Attaching logo

Target Market(s)

Hong Kong based, Chinese, females, 30-50+ age. 90% female clients.

Industry/Entity Type

Beauty Salon

Number of Pages Required

5+ page

Font styles to use
Sans Serif

Colors
f9d9e8
fbd3d4
fee3d5
fbe7d2
fee18a
fbf289
ffffff

Requirements
Must have
• interactive elements on website, such as scrolling banner photo headers
• incorporate photos of website salon
• connect to facebook page

```html
<!DOCTYPE html>
<html lang="en">
<head>
<meta charset="utf-8">
<title>Velvet Bloom – Beauty Salon &amp; Spa</title>
<link rel="stylesheet" href="https://fonts.googleapis.com/css2?family=Courgette&family=Montserrat:wght@400;500;600;700&family=Open+Sans:wght@400;600&display=swap">
<style>
:root{
  --purple:#6e1f80;
  --purple-soft:#8b3d9c;
  --purple-title:#7a2a8c;
  --pink:#e8528f;
  --ink:#333;
  --line:#cfcfcf;
  --white:#fff;
  --contact-bg:#474546;
  --footer-bg:#5c1a6c;
}
*{box-sizing:border-box;margin:0;padding:0}
html,body{width:1200px;height:3509px;overflow:hidden}
body{position:relative;background:var(--white);font-family:"Open Sans",sans-serif;color:var(--ink)}
.abs{position:absolute}
.script{font-family:"Courgette",cursive;font-weight:400}

/* hero */
.hero{left:0;top:0;width:1200px;height:798px;background:linear-gradient(100deg,#2a0c30 0%,#4a1550 35%,#7a2a6e 60%,#b04a86 80%,#5a1c4a 100%)}
.brand{left:63px;top:82px;display:flex;align-items:center;gap:14px;color:var(--white);font-family:"Montserrat",sans-serif;font-weight:600;font-size:34px}
.brand-dot{width:44px;height:44px;border:3px solid var(--white);border-radius:50%}
.nav{left:526px;top:98px;width:620px;height:30px;font-family:"Montserrat",sans-serif;font-weight:600;font-size:15px;color:var(--white)}
.nav a{color:inherit;text-decoration:none;position:absolute;white-space:nowrap}
.nav .active::after{content:"";position:absolute;left:0;right:0;bottom:-18px;height:4px;background:var(--purple-soft)}
.social{left:962px;top:36px;display:flex;gap:7px}
.social span{width:28px;height:28px;border-radius:50%;background:var(--white)}
.hero-title{left:63px;top:262px;color:var(--white);font-size:37px}
.hero-text{left:63px;top:320px;width:520px;color:var(--white);font-size:14px;line-height:26px}
.btn-outline{display:flex;align-items:center;justify-content:center;font-family:"Montserrat",sans-serif;font-size:15px;font-weight:500;border:2px solid}
.hero-btn{left:63px;top:455px;width:230px;height:44px;color:var(--white);border-color:rgba(255,255,255,.85)}
.info-bar{left:63px;top:625px;width:1076px;height:107px;background:rgba(100,22,120,.78)}
.info-item{position:absolute;top:0;height:107px;display:flex;align-items:center;gap:18px;color:var(--white);font-family:"Montserrat",sans-serif}
.info-item h4{font-size:15px;font-weight:700;margin-bottom:4px}
.info-item p{font-size:15px;line-height:21px}

/* services */
.card{top:854px;width:316px;height:234px;border:1px solid #ddd;border-radius:12px;background:var(--white);box-shadow:0 2px 6px rgba(0,0,0,.06)}
.card-img{position:absolute;left:12px;top:12px;width:292px;height:163px}
.card-label{position:absolute;left:0;right:0;top:186px;text-align:center;font-size:32px;color:#222}

/* reveal */
.reveal-title{left:60px;top:1228px;width:500px;text-align:center;color:var(--purple-title);font-size:44px}
.reveal-sub{left:60px;top:1308px;width:500px;text-align:center;font-family:"Montserrat",sans-serif;font-size:15px;color:#444;letter-spacing:.3px}
.divider{height:20px;display:flex;align-items:center;justify-content:center;gap:10px}
.divider i{display:block;width:75px;height:1px;background:var(--line)}
.divider b{width:10px;height:10px;border:1px solid #aaa;transform:rotate(45deg)}
.reveal-text{left:75px;top:1378px;width:470px;text-align:center;font-size:14px;line-height:23px;color:#555}
.reveal-btn{left:222px;top:1509px;width:192px;height:51px;color:#333;border-color:var(--purple)}
.reveal-frame{left:777px;top:1230px;width:264px;height:391px;border:2px solid #222}
.reveal-photo{left:741px;top:1195px;width:268px;height:398px;background:linear-gradient(160deg,#6b5a52,#cfc3bb 55%,#8a7b74)}

/* offer */
.offer-photo{left:520px;top:1693px;width:680px;height:452px;background:linear-gradient(120deg,#c9a58f,#e8cdbd 45%,#b7826a 100%)}
.offer-panel{left:0;top:1693px;width:690px;height:452px;background:var(--purple);border-radius:0 226px 226px 0}
.offer-pill{left:0;top:1745px;width:625px;height:348px;background:var(--purple-soft);border-radius:0 174px 174px 0}
.offer-title{left:63px;top:1790px;color:var(--white);font-size:44px}
.offer-sub{left:63px;top:1864px;color:var(--white);font-family:"Montserrat",sans-serif;font-weight:500;font-size:20px}
.offer-text{left:63px;top:1904px;width:420px;color:var(--white);font-family:"Montserrat",sans-serif;font-weight:500;font-size:13px;line-height:20px}
.offer-btn{left:63px;top:1990px;width:174px;height:52px;background:var(--pink);color:var(--white);font-family:"Montserrat",sans-serif;font-size:13px;font-weight:700;display:flex;align-items:center;justify-content:center}

/* gallery */
.gallery-title{left:0;width:1200px;top:2172px;text-align:center;font-size:38px;color:#111}
.gallery{left:61px;top:2290px;width:1078px;height:477px;display:grid;grid-template-columns:repeat(3,1fr);grid-template-rows:repeat(2,1fr)}

/* contact */
.contact{left:0;top:2830px;width:1200px;height:620px;background:var(--contact-bg)}
.contact-title{left:0;width:1200px;top:2862px;text-align:center;color:var(--white);font-size:42px}
.c-icon{position:absolute;left:80px;width:26px;height:26px;border-radius:50%;background:var(--purple);display:flex;align-items:center;justify-content:center}
.c-text{position:absolute;left:126px;color:var(--white);font-size:17px;line-height:30px}
.c-head{font-weight:600;font-size:18px}
.c-phone{font-size:26px}
.map{left:575px;top:2978px;width:552px;height:378px;background:linear-gradient(135deg,#e9e6df,#dcd8cf 60%,#e6e2d8)}

/* footer */
.footer{left:0;top:3450px;width:1200px;height:59px;background:var(--footer-bg);color:var(--white);font-family:"Montserrat",sans-serif;font-size:14px}
.footer p{position:absolute;left:80px;top:20px}
.footer-social{position:absolute;left:1093px;top:8px;width:44px;height:44px;border-radius:50%;background:var(--white)}
</style>
</head>
<body>

<section class="abs hero" role="img" aria-label="Salon banner photo: woman with long glossy magenta hair in profile against a dark purple background"></section>

<div class="abs brand"><span class="brand-dot"></span>Velvet Bloom</div>

<nav class="abs nav">
  <a class="active" style="left:0">HOME</a>
  <a style="left:112px">ABOUT US</a>
  <a style="left:258px">SHOP</a>
  <a style="left:363px">PRICE LIST</a>
  <a style="left:513px">CONTACT US</a>
</nav>

<div class="abs social" aria-label="Social links"><span></span><span></span><span></span><span></span><span></span></div>

<h1 class="abs hero-title script">Beautiful hair, Healthy you</h1>
<p class="abs hero-text">"We pride ourselves on being able to offer a private salon experience to our clients in the exclusive suburb of Linden Hill, where your hair design and colouring needs will be met with years of experience and current industry training and knowledge".</p>
<a class="abs btn-outline hero-btn">BOOK AN APPOINTMENT</a>

<div class="abs info-bar">
  <div class="info-item" style="left:14px">
    <svg width="60" height="60" viewBox="0 0 60 60" fill="none" stroke="#fff" stroke-width="4"><circle cx="30" cy="30" r="26"/><path d="M30 14v17h12"/></svg>
    <div><h4>OPENING TIMES</h4><p>MONDAY – FRIDAY: 10:30 TO 9:30</p></div>
  </div>
  <div class="info-item" style="left:390px">
    <svg width="48" height="62" viewBox="0 0 48 62"><path d="M24 2C12 2 3 11 3 23c0 16 21 37 21 37s21-21 21-37C45 11 36 2 24 2z" fill="#fff"/><circle cx="24" cy="22" r="8" fill="#6e1f80"/></svg>
    <div><h4>OUR LOCATION</h4><p>19TH FLOOR, JADE LANTERN CENTRE,<br>52-54 ORCHID ROAD</p></div>
  </div>
  <div class="info-item" style="left:795px">
    <svg width="62" height="60" viewBox="0 0 62 60"><rect x="3" y="8" width="56" height="49" fill="none" stroke="#fff" stroke-width="4"/><rect x="3" y="8" width="56" height="12" fill="#fff"/><rect x="14" y="2" width="5" height="12" fill="#fff"/><rect x="43" y="2" width="5" height="12" fill="#fff"/><g fill="#fff"><rect x="11" y="26" width="8" height="7"/><rect x="23" y="26" width="8" height="7"/><rect x="35" y="26" width="8" height="7"/><rect x="47" y="26" width="6" height="7"/><rect x="11" y="38" width="8" height="7"/><rect x="23" y="38" width="8" height="7"/><rect x="35" y="38" width="8" height="7"/><rect x="47" y="38" width="6" height="7"/></g></svg>
    <div><h4>BOOK NOW</h4><p>23418620<br>61527390</p></div>
  </div>
</div>

<article class="abs card" style="left:82px">
  <div class="card-img" role="img" aria-label="Photo of a facial mask treatment" style="background:linear-gradient(135deg,#e6d6cf,#f4ede8 55%,#b89386)"></div>
  <h3 class="card-label script">Facials</h3>
</article>
<article class="abs card" style="left:433px">
  <div class="card-img" role="img" aria-label="Photo of a woman seated for body care" style="background:linear-gradient(135deg,#e7ebee,#cfd5d9 55%,#d8c2b5)"></div>
  <h3 class="card-label script">Body care</h3>
</article>
<article class="abs card" style="left:786px">
  <div class="card-img" role="img" aria-label="Photo of a slim woman in a bright studio" style="background:linear-gradient(135deg,#7ea3cf,#b9cde6 50%,#6d8fc0)"></div>
  <h3 class="card-label script">Thin shape</h3>
</article>

<h2 class="abs reveal-title script">Reveal Your Beauty</h2>
<p class="abs reveal-sub">BOOK AN APPOINTMENT AND WE'LL TAKE CARE OF THE REST</p>
<div class="abs divider" style="left:60px;top:1347px;width:500px"><i></i><b></b><i></i></div>
<p class="abs reveal-text">Duis autem vel eum iriure dolor in hendrerit in putate velit esse molestie consequat, vel illum doloreeu feugiatDuis autem vel eum iriure dolor in hendrerit in putate velit esse molestie consequat, vel illum doloreeu feugiat</p>
<a class="abs btn-outline reveal-btn">LEARN MORE</a>
<div class="abs reveal-frame"></div>
<div class="abs reveal-photo" role="img" aria-label="Photo of a smiling make-up artist holding brushes"></div>

<div class="abs offer-photo" role="img" aria-label="Photo of a woman relaxing during a face massage"></div>
<div class="abs offer-panel"></div>
<div class="abs offer-pill"></div>
<h2 class="abs offer-title script">Our Special Offer</h2>
<p class="abs offer-sub">YOU OWE YOURSELF THIS MOMENT</p>
<p class="abs offer-text">Lorem ipsum dolor sit amet, consectetur adipiscing elit. Morbi hendrerit elit turpis, a porttitor tellus sollicitudin squ ad litora torquent per conubia.</p>
<a class="abs offer-btn">VIEW PACKAGES</a>

<h2 class="abs gallery-title script">Our Gallery</h2>
<div class="abs divider" style="left:500px;top:2242px;width:200px"><i></i><b></b><i></i></div>
<div class="abs gallery">
  <div role="img" aria-label="Portrait of a woman with long dark hair" style="background:linear-gradient(135deg,#d9dbe0,#8f8a8c)"></div>
  <div role="img" aria-label="Portrait of a woman in a red polka-dot top with a blue backdrop" style="background:linear-gradient(135deg,#8aa0b8,#c25e59)"></div>
  <div role="img" aria-label="Portrait of a woman with curly blonde hair" style="background:linear-gradient(135deg,#f1ead7,#d4b679)"></div>
  <div role="img" aria-label="Portrait of a smiling woman outdoors in green foliage" style="background:linear-gradient(135deg,#8fb25a,#5d7a33)"></div>
  <div role="img" aria-label="Portrait of a woman against a wooden wall" style="background:linear-gradient(135deg,#6d4a36,#3f2b22)"></div>
  <div role="img" aria-label="Portrait of a blonde woman on a black background" style="background:linear-gradient(135deg,#141414,#5a4c3a)"></div>
</div>

<section class="abs contact"></section>
<h2 class="abs contact-title script">Contact Us</h2>

<span class="c-icon" style="top:2987px"><svg width="14" height="14" viewBox="0 0 14 14" fill="none" stroke="#fff" stroke-width="1.6"><circle cx="7" cy="7" r="5.5"/><path d="M7 4v3.3h2.5"/></svg></span>
<p class="c-text" style="top:2970px">Monday to Friday: 10:30 am to 9:30 pm<br>Saturday and holidays: 10:30 am to 7:30 pm</p>

<span class="c-icon" style="top:3061px"><svg width="14" height="14" viewBox="0 0 14 14"><path d="M3 1.5l2.2 2.6-1.2 1.6c.8 1.7 2 2.9 3.6 3.7l1.6-1.2 2.6 2.2-1.3 2C6.3 12 2 7.7 1.4 2.8z" fill="#fff"/></svg></span>
<p class="c-text c-head" style="top:3059px">Inquiry hotline</p>
<p class="c-text c-phone" style="top:3101px">+ 23418620, + 6152739</p>

<span class="c-icon" style="top:3174px"><svg width="12" height="15" viewBox="0 0 12 15"><path d="M6 .5C3 .5.8 2.7.8 5.6 .8 9.5 6 14.5 6 14.5s5.2-5 5.2-8.9C11.2 2.7 9 .5 6 .5z" fill="#fff"/><circle cx="6" cy="5.5" r="2" fill="#6e1f80"/></svg></span>
<p class="c-text c-head" style="top:3172px">Address</p>
<p class="c-text" style="top:3208px;line-height:28px">19th Floor, Jade Lantern Centre, 52-54 Orchid<br>Road Harbour Point, Kowloon</p>

<span class="c-icon" style="top:3284px"><svg width="14" height="11" viewBox="0 0 14 11" fill="none" stroke="#fff" stroke-width="1.4"><rect x="1" y="1" width="12" height="9"/><path d="M1 1l6 5 6-5"/></svg></span>
<p class="c-text c-head" style="top:3282px">Email Address</p>
<p class="c-text" style="top:3312px">hello@velvetbloom-hk.example</p>

<div class="abs map" role="img" aria-label="Street map showing the salon location"></div>

<footer class="abs footer">
  <p>Copyright © 2017 Velvet Bloom HK Ltd. All rights reserved.</p>
  <span class="footer-social" aria-label="Social page"></span>
</footer>

</body>
</html>
```